Tallis Ecological Works New Website Design

I need a new website for a Environmental Project Company based in Sydney Australia, working throughout South East Asia.I've attached the company logo, please try & incorporate these colours or use complimentary colours. I've attached a word doc with design brief.I'm going to use Wix, so please ensure files are suitable.Thankyou.

Number of Pages Required

5+ page

Colors

Designer to choose colors to be used in the design.

Requirements
Must have
• Refer to Word Document
Nice to have
• Refer to Word Document
Should not have
• Not to be dark

```html
<!DOCTYPE html>
<html lang="en">
<head>
<meta charset="utf-8">
<title>Tallis Ecological Works</title>
<link href="https://fonts.googleapis.com/css2?family=Quicksand:wght@400;500;600&family=Open+Sans:wght@400;600&display=swap" rel="stylesheet">
<style>
:root{
  --green:#2c4912;
  --green-text:#2f4d14;
  --teal:#1a9e7c;
  --card:#e5e5e5;
  --panel:#e3e3e3;
  --band:#ececec;
  --ink:#444;
  --white:#fff;
}
*{margin:0;padding:0;box-sizing:border-box}
html,body{width:1200px;height:3209px;overflow:hidden;background:var(--white)}
body{position:relative;font-family:"Open Sans",sans-serif;color:var(--ink)}
.abs{position:absolute}
.head{font-family:"Quicksand",sans-serif;color:var(--green-text);font-weight:500}

/* header */
.brand{left:145px;top:26px;display:flex;align-items:center;gap:14px}
.brand-dot{width:76px;height:76px;border-radius:50%;background:var(--green)}
.brand-name{font-family:"Quicksand",sans-serif;font-weight:600;font-size:22px;line-height:1.15;color:var(--green-text);width:160px}
.nav{top:54px;left:523px;display:flex;gap:0;font-size:15px;color:#333}
.nav a{text-decoration:none;color:inherit;margin-right:42px}
.nav a.active{color:var(--teal)}

/* hero */
.hero{left:0;top:128px;width:1119px;height:470px;background:radial-gradient(circle at 33% 45%,#f5c870 0,#c0782a 14%,#4a2a16 38%,#2b1c14 60%,#5a3b22 80%,#2a1a10 100%)}
.hero-bar{left:0;top:598px;width:1119px;height:15px;background:var(--green)}
.slide-arrow{top:345px;width:26px;height:34px;background:rgba(0,0,0,.45)}
.social{left:1150px;top:296px;display:flex;flex-direction:column;gap:22px}
.social span{width:16px;height:16px;border-radius:50%;background:var(--green)}

.statement{background:var(--panel)}
.statement h2{font-family:"Quicksand",sans-serif;font-weight:500;color:var(--green-text);font-size:46px}
.rule{height:3px;width:80px;background:var(--green)}
.statement p{font-size:13px;line-height:1.75;color:#444}
.btn{display:flex;height:35px}
.btn i{width:36px;background:var(--green);display:flex;align-items:center;justify-content:center}
.btn b{flex:1;background:var(--teal);color:#fff;font-weight:400;font-size:13px;display:flex;align-items:center;justify-content:center}

/* products */
.products-band{left:0;top:888px;width:1200px;height:255px;background:var(--green)}
.products-title{left:145px;top:950px;font-family:"Quicksand",sans-serif;color:#fff;font-size:48px;font-weight:500}
.card-frame{width:279px;height:280px;border:2px solid #e1e1e1;background:#fff}
.card{width:279px;height:280px;background:var(--card);padding:22px 16px}
.card h3{font-family:"Quicksand",sans-serif;font-weight:500;color:var(--green-text);font-size:20px;line-height:1.35;margin-top:10px;height:58px}
.card p{font-size:10.5px;line-height:1.7;color:#555;margin-top:6px}
.card .more{margin-top:14px;font-size:12px;color:var(--teal)}
.card .more::before{content:"›";color:var(--green);font-weight:600;margin-right:6px}

/* testimonials */
.testi{left:0;top:1752px;width:1200px;height:474px;background:var(--band);text-align:center}
.testi-bar{left:0;top:2226px;width:1200px;height:16px;background:var(--green)}
.testi h4{font-family:"Quicksand",sans-serif;font-weight:500;font-size:24px;color:var(--green-text);margin-top:72px}
.testi blockquote{font-family:"Quicksand",sans-serif;font-weight:500;font-size:26px;line-height:1.38;color:var(--green-text);width:720px;margin:24px auto 0}
.testi .who{color:var(--teal);font-size:16px;margin-top:24px;line-height:1.6}
.dots{left:570px;top:2132px;display:flex;gap:12px}
.dots span{width:12px;height:12px;border-radius:50%;border:2px solid var(--green)}
.dots span.on{background:var(--green)}

/* contact */
.footer{left:0;top:2648px;width:1200px;height:561px;background:var(--green);color:#fff}
.footer h3{font-family:"Quicksand",sans-serif;font-weight:500;font-size:25px;text-align:center;margin-top:70px}
.field{border-bottom:2px solid #fff;font-size:13px;padding-bottom:10px}
.submit{left:0;width:1200px;top:2942px;text-align:center;color:#fff;font-size:13px}
.info{left:0;width:1200px;top:3053px;text-align:center;color:#fff;font-size:14px}
.copy{left:143px;top:3135px;color:#fff;font-size:11.5px}
.chat{left:8px;top:3168px;color:#fff;font-size:11px}
</style>
</head>
<body>

<header>
  <div class="abs brand"><span class="brand-dot"></span><span class="brand-name">Tallis Ecological Works</span></div>
  <nav class="abs nav">
    <a class="active">Home</a><a>Who We Are</a><a>Services</a><a>Products</a><a>News</a><a>Contact</a>
  </nav>
</header>

<section>
  <div class="abs hero" role="img" aria-label="Hand holding a glowing light bulb surrounded by renewable energy and environment icons, blurred city lights behind"></div>
  <div class="abs hero-bar"></div>
  <div class="abs slide-arrow" style="left:0"><svg width="26" height="34"><path d="M16 10 9 17l7 7" stroke="#fff" stroke-width="2" fill="none"/></svg></div>
  <div class="abs slide-arrow" style="left:1093px"><svg width="26" height="34"><path d="M10 10l7 7-7 7" stroke="#fff" stroke-width="2" fill="none"/></svg></div>
  <div class="abs social" aria-label="Social links"><span></span><span></span><span></span><span></span></div>

  <div class="abs statement" style="left:600px;top:528px;width:455px;height:242px">
    <h2 class="abs" style="left:24px;top:22px">Our Vision</h2>
    <div class="abs rule" style="left:25px;top:110px"></div>
    <p class="abs" style="left:139px;top:100px;width:290px">Our Vision is to make it easy for everyone to minimise their environmental impact by providing information, technology, packaged green solutions &amp; helping innovation flourish</p>
  </div>
  <div class="abs btn" style="left:912px;top:773px;width:143px"><i><svg width="12" height="14"><path d="M3 2l6 5-6 5" stroke="#fff" stroke-width="2.4" fill="none"/></svg></i><b>Read More</b></div>
</section>

<section>
  <div class="abs products-band"></div>
  <h2 class="abs products-title">Our Products</h2>

  <!-- row 1 -->
  <div class="abs card-frame" style="left:157px;top:1047px"></div>
  <div class="abs card-frame" style="left:465px;top:1047px"></div>
  <div class="abs card-frame" style="left:775px;top:1047px"></div>
  <div class="abs card-frame" style="left:157px;top:1390px"></div>
  <div class="abs card-frame" style="left:465px;top:1390px"></div>
  <div class="abs card-frame" style="left:775px;top:1390px"></div>

  <article class="abs card" style="left:145px;top:1035px">
    <svg width="52" height="46" viewBox="0 0 52 46" fill="none" stroke="#2c4912" stroke-width="2"><path d="M4 22h44l-5 20H9z"/><circle cx="16" cy="14" r="6"/><circle cx="30" cy="10" r="7"/><path d="M38 20c2-8 8-10 10-10"/></svg>
    <h3>Sustainable food</h3>
    <p>Etiam mattis augue vehicula odio posuere, sit amet tempus lectus luctus. Nulla facilisi. Etiam vel massa elementum, bibendum tellus venenatis, feugiat massa. Curabitur venenatis lacinia.</p>
    <div class="more">Read More</div>
  </article>
  <article class="abs card" style="left:453px;top:1035px">
    <svg width="52" height="46" viewBox="0 0 52 46" fill="none" stroke="#2c4912" stroke-width="2"><circle cx="26" cy="8" r="4"/><path d="M10 18h32l4 18H6zM8 27h36M19 18l-2 18M33 18l2 18M26 36v8M18 44h16"/></svg>
    <h3>Sustainable / Renewable Power</h3>
    <p>Etiam mattis augue vehicula odio posuere, sit amet tempus lectus luctus. Nulla facilisi. Etiam vel massa elementum, bibendum tellus venenatis, feugiat massa. Curabitur venenatis lacinia.</p>
    <div class="more">Read More</div>
  </article>
  <article class="abs card" style="left:763px;top:1035px">
    <svg width="52" height="46" viewBox="0 0 52 46" fill="none" stroke="#2c4912" stroke-width="2"><path d="M22 6C14 20 10 26 10 32a12 12 0 0 0 24 0c0-6-4-12-12-26z"/><path d="M42 4c-3 5-4 7-4 9a4 4 0 0 0 8 0c0-2-1-4-4-9z"/></svg>
    <h3>Water quality &amp; treatment</h3>
    <p>Etiam mattis augue vehicula odio posuere, sit amet tempus lectus luctus. Nulla facilisi. Etiam vel massa elementum, bibendum tellus venenatis, feugiat massa. Curabitur venenatis lacinia.</p>
    <div class="more">Read More</div>
  </article>

  <!-- row 2 -->
  <article class="abs card" style="left:145px;top:1378px">
    <svg width="60" height="46" viewBox="0 0 60 46" fill="none" stroke="#2c4912" stroke-width="2"><path d="M4 16h36a6 6 0 1 0-6-6M4 24h48a6 6 0 1 1-6 6M10 32h22a5 5 0 1 1-5 5"/></svg>
    <h3>Air quality</h3>
    <p>Etiam mattis augue vehicula odio posuere, sit amet tempus lectus luctus. Nulla facilisi. Etiam vel massa elementum, bibendum tellus venenatis, feugiat massa. Curabitur venenatis lacinia.</p>
    <div class="more">Read More</div>
  </article>
  <article class="abs card" style="left:453px;top:1378px">
    <svg width="52" height="46" viewBox="0 0 52 46" fill="none" stroke="#2c4912" stroke-width="2"><path d="M26 16l-4 28h8zM26 16L14 4M26 16l14-10M26 16l-2 14"/><circle cx="26" cy="16" r="2"/></svg>
    <h3>Investing in green infrastructure &amp; projects</h3>
    <p>Etiam mattis augue vehicula odio posuere, sit amet tempus lectus luctus. Nulla facilisi. Etiam vel massa elementum, bibendum tellus venenatis, feugiat massa. Curabitur venenatis lacinia.</p>
    <div class="more">Read More</div>
  </article>
  <article class="abs card" style="left:763px;top:1378px">
    <svg width="52" height="46" viewBox="0 0 52 46" fill="none" stroke="#2c4912" stroke-width="2"><path d="M4 8h18a4 4 0 0 1 4 4v30a4 4 0 0 0-4-4H4zM48 8H30a4 4 0 0 0-4 4v30a4 4 0 0 1 4-4h18zM8 16h12M8 22h12M8 28h12M32 16h12M32 22h12M32 28h12"/></svg>
    <h3>Education</h3>
    <p>Etiam mattis augue vehicula odio posuere, sit amet tempus lectus luctus. Nulla facilisi. Etiam vel massa elementum, bibendum tellus venenatis, feugiat massa. Curabitur venenatis lacinia.</p>
    <div class="more">Read More</div>
  </article>
</section>

<section>
  <div class="abs testi">
    <h4>Testimonials</h4>
    <blockquote>“ Quisque aliquet ex nec est vestibulum pulvinar. Pellentesque convallis molestie enim sit amet efficitur. Etiam id imperdiet lectus. Vivamus lacus justo, ultrices nec erat ”</blockquote>
    <div class="who">Mara Lind<br>Etiam mattis augue</div>
  </div>
  <svg class="abs" style="left:48px;top:1978px" width="36" height="20"><path d="M34 10H6M14 2 4 10l10 8" stroke="#2c4912" stroke-width="4" fill="none"/></svg>
  <svg class="abs" style="left:1116px;top:1978px" width="36" height="20"><path d="M2 10h28M22 2l10 8-10 8" stroke="#2c4912" stroke-width="4" fill="none"/></svg>
  <div class="abs dots"><span></span><span class="on"></span><span class="on"></span></div>
  <div class="abs testi-bar"></div>
</section>

<section>
  <div class="abs statement" style="left:240px;top:2320px;width:720px;height:210px">
    <h2 class="abs" style="left:90px;top:22px">Our Mission</h2>
    <div class="abs rule" style="left:92px;top:110px"></div>
    <p class="abs" style="left:204px;top:98px;width:430px">Working with people to minimise the environmental impact of humans on the earth without sacrificing lifestyle and helping innovation flourish.</p>
  </div>
  <div class="abs btn" style="left:815px;top:2533px;width:145px"><i><svg width="12" height="14"><path d="M3 2l6 5-6 5" stroke="#fff" stroke-width="2.4" fill="none"/></svg></i><b>Read More</b></div>
</section>

<footer>
  <div class="abs footer"><h3>Contact Us</h3></div>
  <div class="abs field" style="left:263px;top:2778px;width:320px;color:#fff">Name</div>
  <div class="abs field" style="left:615px;top:2778px;width:320px;color:#fff">Email</div>
  <div class="abs field" style="left:263px;top:2842px;width:672px;height:72px;color:#fff">Message</div>
  <div class="abs submit">SUBMIT</div>
  <div class="abs info">24 Building name, Street name, City Zipcode &nbsp; | &nbsp; Phone : 555 204 7719 &nbsp; | &nbsp; Email : info@tallisecologicalworks.com</div>
  <div class="abs copy">Copyright © 2019 &nbsp;Tallis Ecological Works. &nbsp;All rights reserved.</div>
  <svg class="abs" style="left:1034px;top:3134px" width="22" height="14"><path d="M2 12l9-9 9 9" stroke="#fff" stroke-width="2.4" fill="none"/></svg>
  <div class="abs chat">Let's Chat &nbsp;&nbsp;&nbsp;&nbsp;&nbsp;&nbsp;&nbsp;&nbsp;&nbsp;&nbsp;&nbsp;&nbsp;⌃</div>
</footer>

</body>
</html>
```